NOLV.
ALWAYS BESIDE YOU
NOLV. -
Creative Brief
Use specific fonts
any thing which suits with the LOGO provided
Professional
RAHUL MEHTA
MR.
D-47, NORTH PARK-III, GURGAON 122019, HARYANA, INDIA
rahul@nolv.co
www.nolv.co
use logo at centre

```html
<!DOCTYPE html>
<html lang="en">
<head>
<meta charset="utf-8">
<title>NOLV. Business Card</title>
<link rel="stylesheet" href="https://fonts.googleapis.com/css2?family=Open+Sans:wght@400;600;700&display=swap">
<style>
  :root {
    --stage: #2e2e30;
    --card: #ffffff;
    --brand-red: #e0262b;
    --ink: #3a3a3a;
  }
  * { margin: 0; padding: 0; box-sizing: border-box; }
  html, body { width: 1200px; height: 945px; overflow: hidden; }
  body {
    background: var(--stage);
    font-family: "Open Sans", Arial, sans-serif;
    position: relative;
  }
  .card {
    position: absolute;
    background: var(--card);
    border-radius: 26px;
    overflow: hidden;
    box-shadow: 0 6px 18px rgba(0,0,0,.35);
  }
  .card--front { left: 122px; top: 158px; width: 555px; height: 322px; }
  .card--back  { left: 505px; top: 503px; width: 560px; height: 334px; }

  .brand { position: absolute; left: 32px; top: 36px; }
  .brand__row { display: flex; align-items: center; gap: 14px; }
  .brand__mark { width: 54px; height: 54px; background: var(--brand-red); flex: none; }
  .brand__name {
    color: var(--brand-red); font-weight: 700; font-size: 56px;
    line-height: 1; letter-spacing: 2px;
  }
  .brand__tagline {
    margin-top: 6px; padding-left: 68px; color: var(--ink); font-size: 12.5px;
    font-weight: 600; letter-spacing: 1.2px; white-space: nowrap;
  }

  .address {
    position: absolute; left: 154px; top: 158px; font-style: normal;
    font-size: 11.5px; line-height: 16px; color: var(--ink); font-weight: 600;
    white-space: nowrap;
  }
  .contacts {
    position: absolute; left: 154px; top: 204px; list-style: none;
    font-size: 11.5px; color: var(--ink);
  }
  .contacts li { display: flex; align-items: center; gap: 8px; height: 17px; white-space: nowrap; }
  .contacts svg { width: 11px; height: 11px; fill: var(--brand-red); flex: none; }

  .name-band {
    position: absolute; right: 0; top: 193px; width: 202px; height: 38px;
    background: var(--brand-red); border-radius: 19px 0 0 19px;
    display: flex; align-items: center; justify-content: center;
    color: #fff; font-weight: 700; font-size: 16px; letter-spacing: .5px;
    white-space: nowrap;
  }

  .back-brand {
    position: absolute; left: 50%; top: 50%; transform: translate(-50%, -50%);
    display: flex; align-items: center; gap: 14px;
  }
  .back-brand .brand__mark { width: 48px; height: 48px; }
  .back-brand .brand__name { font-size: 52px; }
</style>
</head>
<body>
  <section class="card card--front">
    <div class="brand">
      <div class="brand__row">
        <span class="brand__mark"></span>
        <span class="brand__name">NOLV.</span>
      </div>
      <p class="brand__tagline">ALWAYS BESIDE YOU</p>
    </div>

    <address class="address">
      D-47, NORTH PARK-III, GURGAON 122019<br>
      HARYANA, INDIA.
    </address>

    <ul class="contacts">
      <li><svg viewBox="0 0 12 12"><path d="M2 1h3l1 3-2 1a7 7 0 0 0 3 3l1-2 3 1v3a1 1 0 0 1-1 1A10 10 0 0 1 1 2a1 1 0 0 1 1-1z"/></svg>+91-124-5550182</li>
      <li><svg viewBox="0 0 12 12"><rect x="3" y="0.5" width="6" height="11" rx="1"/></svg>+91-9000555147</li>
      <li><svg viewBox="0 0 12 12"><rect x="1" y="3" width="10" height="7" rx="1"/><rect x="3" y="1" width="6" height="3"/></svg>+91-124-5550376</li>
      <li><svg viewBox="0 0 12 12"><path d="M1 2.5h10v7H1z M1 2.5l5 4 5-4" stroke="#e0262b" stroke-width="1" fill="none"/></svg>rahul@nolv.co</li>
      <li><svg viewBox="0 0 12 12"><circle cx="6" cy="6" r="5"/></svg>www.nolv.co</li>
    </ul>

    <div class="name-band">RAHUL MEHTA</div>
  </section>

  <section class="card card--back">
    <div class="back-brand">
      <span class="brand__mark"></span>
      <span class="brand__name">NOLV.</span>
    </div>
  </section>
</body>
</html>
```